Mining and Labour hire business needs website

need a web page for a business located in country NSW,Australia. we provide labour hire with a background in electrical contracting. i've attached images that i would like used. and a text file with the text to be used

Target Market(s)

mining and resource sector

Industry/Entity Type

Business

Requirements
Must have
• my logo
• Pages: main, about us, labour hire services, electrical services, equipment, employment, contact us
Nice to have
• other photos/images of heavy industry/mining
• background photos in black and white would be good i think.
• photo sliders

```html
<!DOCTYPE html>
<html lang="en">
<head>
<meta charset="utf-8">
<title>Ridgeline Industry Services</title>
<link href="https://fonts.googleapis.com/css2?family=Roboto:wght@300;400;500;700&display=swap" rel="stylesheet">
<style>
:root{
  --gold:#c9a264;
  --gold-dark:#b08a4e;
  --bar:#8f7444;
  --ink:#222;
  --muted:#555;
  --white:#fff;
  --blue:#2f7fc1;
  --line:#ddd;
}
*{box-sizing:border-box;margin:0;padding:0}
html,body{width:1200px;height:2571px;overflow:hidden;background:#fff}
body{font-family:'Roboto',sans-serif;color:var(--ink);position:relative}
.abs{position:absolute}

/* header */
.site-header{position:absolute;left:0;top:0;width:1200px;height:54px;background:#fff}
.brand{position:absolute;left:86px;top:12px;display:flex;align-items:center;gap:10px;font-weight:700;font-size:22px;color:#333}
.brand-mark{width:28px;height:28px;background:var(--gold)}
.nav{position:absolute;left:316px;top:20px;display:flex;gap:22px;font-size:14px;color:#444}
.nav .active{color:var(--gold)}
.search{position:absolute;left:1000px;top:14px;width:114px;height:28px;border:1px solid #ccc;font-size:12px;color:#999;padding:6px 8px}

/* hero */
.hero{position:absolute;left:0;top:54px;width:1200px;height:506px;background:linear-gradient(160deg,#6e5a42 0%,#8b6d4a 35%,#a27a4c 60%,#5a4635 100%)}
.hero-kicker{position:absolute;left:206px;top:34px;font-size:20px;color:#fff}
.hero-title{position:absolute;left:204px;top:62px;font-size:52px;font-weight:500;color:#fff}
.hero-text{position:absolute;left:206px;top:134px;width:500px;font-size:19px;font-weight:500;line-height:29px;color:#fff}
.btn-quote{position:absolute;left:206px;top:352px;width:194px;height:58px;background:var(--gold);color:#fff;font-size:22px;display:flex;align-items:center;justify-content:center}
.slide-arrow{position:absolute;top:233px;width:36px;height:36px;border-radius:50%;background:#fff}

/* about */
.section-title{position:absolute;width:1200px;left:0;text-align:center;color:var(--gold);font-size:34px;font-weight:500}
.divider{position:absolute;left:540px;width:120px;height:1px}
.divider-dark{background:#555}
.divider-light{background:#fff}
.about-text{position:absolute;left:243px;top:682px;width:714px;text-align:center;font-size:12.5px;line-height:24px;color:#333}
.photo{position:absolute}

/* band */
.band{position:absolute;left:0;top:1028px;width:1200px;height:406px;background:linear-gradient(135deg,#c9a264 0%,#d2ad70 40%,#b89258 100%)}
.band-title{position:absolute;left:0;top:56px;width:1200px;text-align:center;color:#fff;font-size:28px;font-weight:500}
.band-text{position:absolute;left:240px;top:126px;width:720px;text-align:center;color:#fff;font-size:15px;line-height:24px}
.circle{position:absolute;top:210px;width:138px;height:138px;border-radius:50%;border:3px solid #fff}

/* best */
.best-title{position:absolute;left:600px;top:1496px;color:var(--gold);font-size:28px;font-weight:500}
.best-text{position:absolute;left:600px;width:500px;font-size:12.5px;line-height:24px;color:#333}
.ticks{position:absolute;left:600px;top:1692px;list-style:none;font-size:12.5px;color:#333}
.ticks li{height:28px;display:flex;align-items:center;gap:12px}
.ticks li::before{content:"";width:9px;height:9px;border-radius:50%;background:var(--gold)}

/* newsletter */
.newsletter{position:absolute;left:114px;top:1877px;width:977px;height:266px;border:6px dashed #e6e6e6}
.news-title{position:absolute;left:0;top:50px;width:965px;text-align:center;font-size:26px;font-weight:300;color:#222}
.field{position:absolute;top:101px;height:42px;border:1px solid #ccc;font-size:12px;color:#999;padding:13px 10px}
.btn-sub{position:absolute;left:726px;top:101px;width:84px;height:42px;background:var(--blue);color:#fff;font-size:11px;display:flex;align-items:center;justify-content:center}
.news-note{position:absolute;left:0;top:184px;width:965px;text-align:center;font-size:11px;color:#555}

/* footer */
.site-footer{position:absolute;left:0;top:2214px;width:1200px;height:306px;background:var(--gold);color:#fff}
.foot-col h3{font-size:26px;font-weight:400;margin-bottom:18px}
.foot-col li{list-style:none;font-size:15px;line-height:30px}
.contact-row{display:flex;gap:14px;font-size:11px;line-height:20px;margin-bottom:20px;white-space:nowrap}
.map{position:absolute;left:734px;top:43px;width:380px;height:223px;background:linear-gradient(135deg,#eceae4,#dcdad2)}
.bottom-bar{position:absolute;left:0;top:2520px;width:1200px;height:51px;background:var(--bar);color:#fff;font-size:12px}
.social{position:absolute;top:16px;width:20px;height:20px;border-radius:50%;border:1px solid #fff}
</style>
</head>
<body>

<header class="site-header">
  <div class="brand"><span class="brand-mark"></span>Ridgeline</div>
  <nav class="nav">
    <span class="active">Home</span><span>About us</span><span>Labour hire services</span><span>Electrical services</span><span>Equipment</span><span>Employment</span><span>Contact us</span>
  </nav>
  <div class="search">Search</div>
</header>

<section class="hero" role="img" aria-label="Slider photo of a large mining haul truck at sunset">
  <div class="hero-kicker">We start work with us</div>
  <h1 class="hero-title">Great Vision</h1>
  <p class="hero-text">Lorem Ipsum is simply dummy text of the printing and type-setting industry. Lorem Ipsum has been the industry's&nbsp; Lorem Ipsum has been the industry's</p>
  <div class="btn-quote">Free Quote</div>
  <svg class="slide-arrow" style="left:88px" viewBox="0 0 36 36"><path d="M21 11l-7 7 7 7" stroke="#222" stroke-width="3" fill="none"/></svg>
  <svg class="slide-arrow" style="left:1073px" viewBox="0 0 36 36"><path d="M15 11l7 7-7 7" stroke="#222" stroke-width="3" fill="none"/></svg>
</section>

<section class="about">
  <h2 class="section-title" style="top:602px">About us</h2>
  <div class="divider divider-dark" style="top:656px"></div>
  <p class="about-text">Lorem ipsum is simply dummy text of the printing and typesetting industry. Lorem Ipsum has been the industry's standard dummy text ever since the 1500s, when an unknown printer took a galley of type and scrambled it to make a type specimen book, when an unknown printer took a galley of type and scrambled it to make a type specimen book.</p>
  <div class="photo" style="left:260px;top:786px;width:323px;height:180px;background:linear-gradient(180deg,#7fa6d6,#c79a6a 60%,#8a5a3a)" role="img" aria-label="Photo of a miner statue in front of a headframe"></div>
  <div class="photo" style="left:614px;top:786px;width:326px;height:180px;background:linear-gradient(180deg,#5a7fb2,#b45a32 55%,#7a3a22)" role="img" aria-label="Photo of a large rusted town sign on a hillside"></div>
</section>

<section class="band" role="img" aria-label="Faded background photo of a miner statue and headframe">
  <h2 class="band-title">Lorem Ipsum is simply dummy text</h2>
  <div class="divider divider-light" style="top:106px"></div>
  <p class="band-text">Lorem Ipsum is simply dummy text of the printing and typesetting industry. Lorem Ipsum has been the industry's standard dummy text ever since the 1500s.</p>
  <svg class="circle" style="left:317px" viewBox="0 0 138 138" role="img" aria-label="Photo of a conveyor belt"><circle cx="69" cy="69" r="69" fill="#3a3a3a"/><path d="M69 52v34M52 69h34" stroke="#fff" stroke-width="4"/></svg>
  <div class="circle" style="left:517px;background:#4a4e56" role="img" aria-label="Photo of an electrical switchboard"></div>
  <div class="circle" style="left:717px;background:radial-gradient(circle,#b8902e,#2a2a2a)" role="img" aria-label="Photo of a mining loader"></div>
</section>

<section class="best">
  <div class="photo" style="left:86px;top:1506px;width:471px;height:308px;background:linear-gradient(180deg,#5f93d0 0%,#9cbbe0 45%,#7a6a55 70%,#5b4c3a 100%)" role="img" aria-label="Photo of a mine headframe and conveyor gantry"></div>
  <h2 class="best-title">We are the best in business</h2>
  <p class="best-text" style="top:1542px">Lorem Ipsum is simply dummy text of the printing and typesetting industry. Lorem Ipsum has been the industry's standard dummy text ever since the 1500s, when an unknown printer took a galley of type and scrambled it to make a type specimen book.</p>
  <p class="best-text" style="top:1630px">Lorem Ipsum is simply dummy text of the printing and typesetting industry. Lorem Ipsum has been the industry's standard dummy text ever since the 1500s,</p>
  <ul class="ticks">
    <li>Lorem Ipsum is simply dummy text of the printing</li>
    <li>Lorem Ipsum is simply dummy text of the printing</li>
    <li>Lorem Ipsum is simply dummy text of the printing</li>
    <li>Lorem Ipsum is simply dummy text of the printing</li>
  </ul>
</section>

<section class="newsletter">
  <h2 class="news-title">NEWSLETTER SUBSCRIPTION</h2>
  <div class="field" style="left:171px;width:270px">Enter Name</div>
  <div class="field" style="left:447px;width:277px">Enter Email</div>
  <div class="btn-sub">SUBSCRIBE</div>
  <p class="news-note">&#9673; Get to know the latest news and offer we provide on the site. We don't spam</p>
</section>

<footer class="site-footer">
  <div class="foot-col abs" style="left:86px;top:28px">
    <h3>Services</h3>
    <ul><li>labour hire</li><li>electrical</li><li>labour hire</li><li>electrical</li><li>labour hire</li><li>electrical</li></ul>
  </div>
  <div class="foot-col abs" style="left:246px;top:28px">
    <h3>Solutions</h3>
    <ul><li>Lorem Ipsum</li><li>Lorem Ipsum</li><li>Lorem Ipsum</li><li>Lorem Ipsum</li><li>Lorem Ipsum</li><li>Lorem Ipsum</li></ul>
  </div>
  <div class="foot-col abs" style="left:420px;top:28px;width:306px">
    <h3>Contact us</h3>
    <div class="contact-row">
      <svg width="16" height="22" viewBox="0 0 16 22"><path d="M8 0a8 8 0 0 0-8 8c0 6 8 14 8 14s8-8 8-14a8 8 0 0 0-8-8z" fill="#fff"/><circle cx="8" cy="8" r="3" fill="#c9a264"/></svg>
      <div>Street: 14 Quarry Rd, Westbrook NSW 2899<br>Postal address: PO Box 210, Westbrook NSW 2899<br>Delivery Address: 14 Quarry Rd, Westbrook NSW 2899<br>Director</div>
    </div>
    <div class="contact-row">
      <svg width="18" height="18" viewBox="0 0 24 24"><path d="M6.6 10.8a15 15 0 0 0 6.6 6.6l2.2-2.2a1 1 0 0 1 1-.25 11 11 0 0 0 3.6.6 1 1 0 0 1 1 1V20a1 1 0 0 1-1 1A17 17 0 0 1 3 4a1 1 0 0 1 1-1h3.5a1 1 0 0 1 1 1 11 11 0 0 0 .6 3.6 1 1 0 0 1-.25 1z" fill="#fff"/></svg>
      <div style="font-size:14px;line-height:22px">+61 2 5550 1842<br>+61 2 5550 1843</div>
    </div>
  </div>
  <div class="map" role="img" aria-label="Street map showing the office location"></div>
</footer>

<div class="bottom-bar">
  <span class="abs" style="left:86px;top:18px">COPYRIGHT 2015 © RIDGELINE . ALL RIGHTS RESERVED.</span>
  <span class="social" style="left:944px"></span>
  <span class="social" style="left:970px"></span>
  <span class="social" style="left:996px"></span>
  <span class="social" style="left:1022px"></span>
  <span class="social" style="left:1048px"></span>
  <span class="social" style="left:1074px"></span>
</div>

</body>
</html>
```